wine label design

i'm a fine wine store based in new zealand which buys quality bulk wine and bottles it, passing on the significant savings onto the customer. i require a brand name and design which is cool/ sharp and contempory. the wines will be all still wines, there won't be any sparkling wines under this brand. i've used brand names like harbourlight wine company for previous designs/label but want something more edgier. we thought about a brand name 'sky above the vines' or 'harbourlight wine co' but couldn't get a design to match the title of brand, if you have any thoughts on this send thru your design. take into account color they have to be bold as i am printing these thru a digital printer. the label is a wrap around design, the dimensions are approximately 80 or 90 mm high and 210 mm wide. have a look at these links, i think they have some x-factor to them: http://www.marlowvale.example/store/product_images/p/855/velora__34476_zoom.jpg: OR

http://static3.cellarfinder.example/images/labels/35/24/ember-in-the-fog-shiraz-petite-sirah-south-australia-10203524.jpg: OR

http://www.bottlebarn.example/ui/productimages/25223/25223_w240.jpg: OR

http://www.vintrail.example/images/viewWinery.php?pic=238291

Take into account i have to be able put a wine desription on the back label, barcode and a few technical details required by law. on the front label all i require is space to put the grape variety, area and vintage. i need the grape type to really stand out.
Updates

Reason: hi, the designs coming thru look good, just need a little more changes, also please read thru the brief, there are a few things i have noted such as label size etc etc

Target Market(s)

am after a label the cool/edgy/contempoary that appeals to the educated well off customer that willing to give something new a go by the look of the label that is cool and edgy.

Industry/Entity Type

Boutique

Requirements
Must have
• bold bold bold, it must stand out on the shelf
Nice to have
• a title/brand name that links what i'm doing, from what i'm doing the name 'harbourlight wine co' is probably best suited.
Should not have
• basic boring artwork and small text, the bigger the text the better

```html
<!DOCTYPE html>
<html lang="en">
<head>
<meta charset="utf-8">
<title>Harbourlight Wine Co – Cabernet Sauvignon Label</title>
<link rel="stylesheet" href="https://fonts.googleapis.com/css2?family=Anton&family=Crimson+Pro:ital,wght@0,400;1,400;1,600&family=Open+Sans:wght@400&display=swap">
<style>
  :root {
    --page: #ffffff;
    --caption: #9a9a9a;
    --wrap-gold: #d9c27a;
    --panel-gold: #b8983f;
    --panel-edge: #dcc273;
    --frame-ink: #2a2520;
    --vintage-yellow: #f2c830;
    --variety-ink: #3a3123;
    --detail-ink: #2f2a22;
    --cream-box: #f2e7d8;
    --grape-purple: #4a1f5c;
    --leaf-green: #3f8a5a;
  }
  * { box-sizing: border-box; margin: 0; padding: 0; }
  html, body {
    width: 1200px; height: 960px; overflow: hidden;
    background: var(--page);
  }
  .canvas { position: relative; width: 1200px; height: 960px; overflow: hidden; }

  .caption {
    position: absolute;
    font-family: "Open Sans", sans-serif;
    font-size: 18px;
    color: var(--caption);
    white-space: nowrap;
  }
  .caption--closeup { left: 526px; top: 91px; }
  .caption--full { left: 1003px; top: 403px; }

  /* Full wrap-around label, softened behind the close-up */
  .full-label {
    position: absolute;
    left: -10px; top: 434px; width: 1220px; height: 490px;
    background: var(--wrap-gold);
    filter: blur(3px);
  }
  .full-label__cream-box {
    position: absolute; left: 39px; top: 404px; width: 225px; height: 79px;
    background: var(--cream-box); border-radius: 10px;
  }
  .full-label__center {
    position: absolute; left: 298px; top: 5px; width: 626px; height: 483px;
    background: var(--panel-gold);
    border: 5px solid var(--frame-ink);
  }
  .full-label__brand {
    position: absolute; right: 20px; top: 20px;
    font-family: "Anton", sans-serif; font-size: 62px; line-height: 1;
    color: var(--frame-ink);
  }
  .full-label__art {
    position: absolute; left: 150px; top: 210px; width: 200px; height: 60px;
    background: linear-gradient(90deg, var(--grape-purple), #6b3a82 50%, var(--leaf-green));
    border-radius: 30px;
  }
  .full-label__vintage {
    position: absolute; left: 0; right: 0; top: 350px; text-align: center;
    font-family: "Crimson Pro", serif; font-style: italic; font-size: 30px;
    color: var(--vintage-yellow);
  }
  .full-label__variety {
    position: absolute; left: 0; right: 0; top: 388px; text-align: center;
    font-family: "Crimson Pro", serif; font-style: italic; font-weight: 600; font-size: 32px;
    color: var(--variety-ink);
  }
  .full-label__details {
    position: absolute; left: 18px; right: 18px; top: 446px;
    display: flex; justify-content: space-between;
    font-family: "Crimson Pro", serif; font-size: 19px; color: var(--detail-ink);
  }
  .full-label__back-copy {
    position: absolute; left: 942px; top: 40px; width: 245px;
    font-family: "Crimson Pro", serif; font-size: 15px; line-height: 1.3;
    color: var(--detail-ink);
  }
  .full-label__bottler {
    position: absolute; left: 942px; top: 452px;
    font-family: "Crimson Pro", serif; font-size: 16px; color: var(--detail-ink);
  }

  /* Close-up front panel */
  .front-panel {
    position: absolute; left: 22px; top: 134px; width: 780px; height: 603px;
    background: var(--panel-gold);
    border: 4px solid var(--panel-edge);
    box-shadow: 10px 12px 14px rgba(0, 0, 0, 0.55);
  }
  .front-panel__frame {
    position: absolute; inset: 6px;
    border: 6px solid var(--frame-ink);
  }
  .front-panel__brand {
    position: absolute; left: 0; right: 0; top: 28px; text-align: center;
    font-family: "Anton", sans-serif; font-size: 80px; line-height: 1;
    letter-spacing: -1px;
    color: var(--frame-ink);
    white-space: nowrap;
  }
  .front-panel__art {
    position: absolute; left: 188px; top: 150px; width: 420px; height: 272px;
  }
  .front-panel__vintage {
    position: absolute; left: 0; right: 24px; top: 417px; text-align: center;
    font-family: "Crimson Pro", serif; font-style: italic; font-size: 38px;
    color: var(--vintage-yellow);
  }
  .front-panel__variety {
    position: absolute; left: 0; right: 24px; top: 467px; text-align: center;
    font-family: "Crimson Pro", serif; font-style: italic; font-weight: 600; font-size: 40px;
    color: var(--variety-ink);
  }
  .front-panel__details {
    position: absolute; left: 26px; right: 26px; top: 544px;
    display: flex; justify-content: space-between;
    font-family: "Crimson Pro", serif; font-size: 23px; color: var(--detail-ink);
  }
</style>
</head>
<body>
<div class="canvas">

  <p class="caption caption--closeup">Close-up of Label Center Panel</p>
  <p class="caption caption--full">Full Label</p>

  <div class="full-label" aria-hidden="true">
    <div class="full-label__cream-box"></div>
    <div class="full-label__center">
      <div class="full-label__brand">HARBOURLIGHT WINE CO</div>
      <div class="full-label__art"></div>
      <div class="full-label__vintage">2008</div>
      <div class="full-label__variety">Cabernet Sauvignon</div>
      <div class="full-label__details">
        <span>14% Alc./Vol</span>
        <span>Product of New Zealand</span>
        <span>750 ml.</span>
      </div>
    </div>
    <p class="full-label__back-copy">Harvested from sunny hillside blocks, this wine shows dark berry fruit, gentle oak and a long, smooth finish. Best enjoyed young.</p>
    <p class="full-label__bottler">Bottled by Harbourlight Wine Co.</p>
  </div>

  <section class="front-panel">
    <div class="front-panel__frame"></div>
    <h1 class="front-panel__brand">HARBOURLIGHT WINE CO</h1>

    <svg class="front-panel__art" viewBox="0 0 420 272" role="img" aria-label="Illustration of a purple grape cluster beside a green vine leaf">
      <defs>
        <linearGradient id="grape-leaf-tones" x1="0" y1="0" x2="1" y2="0">
          <stop offset="0" stop-color="#4a1f5c"/>
          <stop offset="0.45" stop-color="#6b3a82"/>
          <stop offset="0.6" stop-color="#5f9a6e"/>
          <stop offset="1" stop-color="#3f8a5a"/>
        </linearGradient>
      </defs>
      <rect x="0" y="0" width="420" height="272" rx="60" fill="url(#grape-leaf-tones)"/>
    </svg>

    <p class="front-panel__vintage">2008</p>
    <h2 class="front-panel__variety">Cabernet Sauvignon</h2>
    <div class="front-panel__details">
      <span>14% Alc./Vol</span>
      <span>Product of New Zealand</span>
      <span>750 ml.</span>
    </div>
  </section>

</div>
</body>
</html>
```